Psychotherapist need a business card with logo

I am a psychotherapist in need of a business card. The card must have:

Marisol Trevuneda
Psicoterapeuta
937 281 706

Psychologists use the greek letter psy, which is the psychologist symbol, but I would prefer something like a mandala, a graphic symbol, an iconic tree, nothing very usual, but something that shows confidence and trust.

Industry/Entity Type

Business

```html
<!DOCTYPE html>
<html lang="es">
<head>
<meta charset="utf-8">
<title>Marisol Trevuneda · Psicoterapeuta</title>
<link rel="stylesheet" href="https://fonts.googleapis.com/css2?family=Open+Sans:wght@400;700&display=swap">
<style>
  :root {
    --paper: #ffffff;
    --ink-dark: #1f1f1f;
    --ink-light: #ffffff;
    --magenta: #e5247b;
    --cyan: #29abe2;
    --lime: #8cc63f;
  }
  html, body {
    margin: 0;
    padding: 0;
    width: 1200px;
    height: 702px;
    overflow: hidden;
    background: var(--paper);
  }
  .card {
    position: relative;
    width: 1200px;
    height: 702px;
    background: var(--paper);
    font-family: "Open Sans", Arial, sans-serif;
    overflow: hidden;
  }
  .stripes {
    position: absolute;
    top: 224px;
    width: 465px;
    height: 70px;
  }
  .stripes--left { left: 0; }
  .stripes--right { right: 0; }
  .stripe {
    position: absolute;
    left: 0;
    width: 100%;
    height: 13px;
  }
  .stripe--magenta { top: 0; background: var(--magenta); }
  .stripe--cyan { top: 28px; background: var(--cyan); }
  .stripe--lime { top: 56px; background: var(--lime); }

  .brand {
    position: absolute;
    left: 465px;
    top: 100px;
    width: 270px;
    display: flex;
    flex-direction: column;
    align-items: center;
  }
  .brand__dot {
    width: 120px;
    height: 120px;
    border-radius: 50%;
    background: var(--magenta);
  }
  .brand__name {
    margin-top: 22px;
    font-size: 22px;
    font-weight: 700;
    color: var(--ink-dark);
    white-space: nowrap;
  }

  .base {
    position: absolute;
    left: 0;
    top: 382px;
    width: 1200px;
    height: 320px;
    background: var(--ink-dark);
    color: var(--ink-light);
  }
  .identity {
    position: absolute;
    left: 57px;
    top: 110px;
  }
  .identity__name {
    margin: 0;
    font-size: 35px;
    font-weight: 700;
    line-height: 1.05;
  }
  .identity__role {
    margin: 0;
    font-size: 32px;
    font-weight: 400;
    line-height: 1.15;
  }
  .contact {
    position: absolute;
    right: 57px;
    top: 130px;
    margin: 0;
    font-size: 35px;
    font-weight: 400;
  }
  .contact__label { font-weight: 700; }
</style>
</head>
<body>
<main class="card">
  <div class="stripes stripes--left">
    <span class="stripe stripe--magenta"></span>
    <span class="stripe stripe--cyan"></span>
    <span class="stripe stripe--lime"></span>
  </div>

  <div class="brand">
    <span class="brand__dot"></span>
    <span class="brand__name">Marisol Trevuneda</span>
  </div>

  <div class="stripes stripes--right">
    <span class="stripe stripe--magenta"></span>
    <span class="stripe stripe--cyan"></span>
    <span class="stripe stripe--lime"></span>
  </div>

  <section class="base">
    <div class="identity">
      <h1 class="identity__name">Marisol Trevuneda</h1>
      <p class="identity__role">Psicoterapeuta</p>
    </div>
    <p class="contact"><span class="contact__label">Tel:</span> 937 281 706</p>
  </section>
</main>
</body>
</html>
```